Web Page Re-designed

Looking to have this portion of a webpage on my site re-designed to look a little more clean and professional, the layout and organization of the data can be changed for example the location name does not have to keep repeating itself its schedule for a sports league

Reason: Still looking fo the right design

It Professional

```html
<!DOCTYPE html>
<html lang="en">
<head>
<meta charset="utf-8">
<title>Ridgeline Sports – Wednesday Co-ed Ball Hockey Schedule</title>
<link href="https://fonts.googleapis.com/css2?family=Oswald:wght@500&family=Questrial&display=swap" rel="stylesheet">
<style>
:root{
  --bg:#8cc043;
  --bg-light:#b3d86a;
  --panel:#b3c95a;
  --dark:#464646;
  --yellow:#fde36b;
  --cream:#fcfcf7;
  --text:#2f2f2f;
  --rule:#c9c9c9;
  --white:#ffffff;
  --blue:#1f4e9a;
  --red:#c8141a;
  --gold:#e8b62c;
}
*{box-sizing:border-box;margin:0;padding:0}
html,body{width:1161px;height:1200px;overflow:hidden;background:var(--bg)}
body{font-family:"Questrial",sans-serif;color:var(--text)}
.page{position:absolute;left:0;top:0;width:1324px;height:1368px;transform:scale(0.8769);transform-origin:0 0;
  background:radial-gradient(ellipse 700px 520px at 660px 380px,var(--bg-light),var(--bg) 85%)}
.abs{position:absolute}
.brand{left:100px;top:64px;width:240px;font-family:"Questrial",sans-serif;font-size:30px;line-height:36px;color:var(--white);white-space:nowrap}
.nav a{position:absolute;top:68px;padding-top:12px;border-top:1px solid rgba(255,255,255,.6);font-family:"Oswald",sans-serif;font-size:20px;color:var(--white);text-decoration:none;text-align:center}
.nav a.active{border-top:3px solid var(--white);padding-top:10px}
.side-menu a{position:absolute;left:88px;width:238px;height:32px;border:2px solid #a9d66b;background:#7fb53a;box-shadow:0 0 12px rgba(255,255,255,.45);color:#2f3a14;text-decoration:none;font-size:17px;line-height:28px;text-align:center;padding-left:50px}
.hero{left:381px;top:150px;width:831px;height:163px;background:linear-gradient(180deg,rgba(140,192,67,0) 0%,#b99a7a 55%,#b8272a 100%)}
.social-bar{left:610px;top:281px;width:398px;height:32px;background:var(--blue);border-radius:6px 6px 0 0;color:var(--white);font-size:19px;letter-spacing:1.5px;display:flex;align-items:center;justify-content:center;gap:10px}
.social-bar .dot{width:26px;height:26px;border-radius:50%;background:var(--white)}
.title-bar{left:381px;top:314px;width:830px;height:39px;background:var(--white);border-top:5px solid #5a8f22;border-radius:0 0 6px 6px}
.title-bar .league{position:absolute;left:26px;top:6px;font-size:17px;font-variant:small-caps;text-decoration:underline;color:#333}
.title-bar .season{position:absolute;left:607px;top:6px;font-size:17px;font-variant:small-caps}
.season-select{position:absolute;left:668px;top:7px;width:124px;height:23px;background:#2b2b2b;color:var(--white);font-size:15px;padding:2px 5px}
.season-select .arrow{position:absolute;right:0;top:0;width:22px;height:23px;background:var(--yellow);border:1px solid #888}
.season-select .arrow:after{content:"";position:absolute;left:4px;top:6px;border-left:7px solid transparent;border-right:7px solid transparent;border-top:11px solid #222}
.filter{top:397px;height:35px;background:var(--dark);border-radius:8px 8px 0 0;color:var(--white);font-size:17px;line-height:36px;text-align:center}
.filter:after{content:"";position:absolute;right:16px;top:11px;border-left:7px solid transparent;border-right:7px solid transparent;border-top:13px solid var(--white)}
.content{left:85px;top:432px;width:1123px;height:825px;background:var(--panel)}
.day{position:absolute;left:6px;width:835px}
.day .date{position:absolute;left:2px;top:0;height:29px;padding:0 8px;background:var(--cream);border:1px solid #777;font-size:14px;line-height:30px;letter-spacing:1px;text-transform:uppercase}
.day .table{position:absolute;left:0;top:33px;width:835px;height:158px;background:var(--cream);border:1px solid #777}
.thead{position:absolute;left:0;top:0;width:833px;height:24px;background:var(--yellow);border-bottom:1px solid #777;font-size:17px;line-height:25px}
.thead span,.row span{position:absolute;white-space:nowrap}
.row{position:absolute;left:0;width:833px;height:39px;font-size:17px;letter-spacing:.8px;line-height:39px}
.row:not(.last):after{content:"";position:absolute;left:10px;right:8px;bottom:0;border-bottom:1px solid var(--rule)}
.row i{position:absolute;top:8px;height:24px;border-left:1px solid #9a9a9a}
.row svg{position:absolute;top:8px;width:24px;height:22px}
.box{position:absolute;left:871px;width:242px;border:1px solid #888;background:var(--panel)}
.box h3{height:32px;background:var(--dark);color:var(--white);font-weight:normal;font-size:17px;line-height:34px;padding-left:29px;border-radius:6px 6px 0 0}
.box ul{list-style:none;padding:4px 0 6px 24px}
.box li{font-size:16px;line-height:23px;letter-spacing:.5px;padding-left:24px;position:relative}
.box li:before{content:"";position:absolute;left:0;top:7px;width:6px;height:6px;border:2px solid var(--white);border-radius:50%}
.login{left:871px;top:543px;width:242px;height:32px;background:var(--dark);border-radius:6px 6px 0 0;color:var(--white);font-size:17px;line-height:34px;padding-left:37px}
.footer{left:0;top:1306px;width:1304px;text-align:center;color:var(--white);font-size:16px;letter-spacing:.5px}
</style>
</head>
<body>
<svg width="0" height="0" style="position:absolute">
  <symbol id="jersey" viewBox="0 0 24 22"><path d="M7 1h10l6 4-3 5-3-2v13H7V8l-3 2-3-5z"/></symbol>
</svg>
<div class="page">
  <div class="abs brand">Ridgeline Sports</div>

  <nav class="nav">
    <a style="left:384px;width:86px">LEAGUES</a>
    <a class="active" style="left:518px;width:158px">SCHEDULES &amp; MORE</a>
    <a style="left:732px;width:86px">REGISTER</a>
    <a style="left:860px;width:60px">PAY</a>
    <a style="left:960px;width:80px">FORUM</a>
    <a style="left:1090px;width:120px">TOURNAMENTS</a>
  </nav>

  <div class="side-menu">
    <a style="top:138px">HOME</a>
    <a style="top:176px">ABOUT US</a>
    <a style="top:213px">FAQS</a>
    <a style="top:251px">CONTACT US</a>
    <a style="top:289px">JOBS</a>
    <a style="top:327px">SPONSORS</a>
  </div>

  <div class="abs hero" role="img" aria-label="Photo strip of seven league players in hockey, baseball and team jerseys"></div>
  <div class="abs social-bar"><span class="dot"></span>Find us on Social</div>

  <div class="abs title-bar">
    <span class="league">Wednesday Co-ed Ball Hockey Schedule</span>
    <span class="season">Season</span>
    <div class="season-select">FALL 2013<span class="arrow"></span></div>
  </div>

  <div class="abs filter" style="left:85px;width:398px">- SELECT TEAM -</div>
  <div class="abs filter" style="left:528px;width:398px">REGULAR SEASON/EXHIBITION</div>

  <main class="abs content">
    <section class="day" style="top:7px">
      <div class="date">Wednesday Oct 6th</div>
      <div class="table">
        <div class="thead"><span style="left:57px">TIME</span><span style="left:161px">HOME</span><span style="left:385px">AWAY</span><span style="left:580px">LOCATION</span><span style="left:732px">STICK</span></div>
        <div class="row" style="top:25px"><span style="left:12px">RS</span><span style="left:48px">8:00pm</span><i style="left:133px"></i><span style="left:164px">KODIAK</span><i style="left:246px"></i><svg style="left:273px;fill:var(--gold)"><use href="#jersey"/></svg><span style="left:302px">vs.</span><i style="left:339px"></i><span style="left:352px">Top Shelf Crew</span><i style="left:487px"></i><svg style="left:502px;fill:var(--red)"><use href="#jersey"/></svg><i style="left:543px"></i><span style="left:561px">Maple Centre</span><i style="left:703px"></i></div>
        <div class="row" style="top:64px"><span style="left:12px">RS</span><span style="left:48px">8:00pm</span><i style="left:133px"></i><span style="left:164px">KODIAK</span><i style="left:246px"></i><svg style="left:273px;fill:var(--gold)"><use href="#jersey"/></svg><span style="left:302px">vs.</span><i style="left:339px"></i><span style="left:352px">Top Shelf Crew</span><i style="left:487px"></i><svg style="left:502px;fill:var(--red)"><use href="#jersey"/></svg><i style="left:543px"></i><span style="left:561px">Maple Centre</span><i style="left:703px"></i></div>
        <div class="row last" style="top:103px"><span style="left:12px">RS</span><span style="left:48px">8:00pm</span><i style="left:133px"></i><span style="left:164px">KODIAK</span><i style="left:246px"></i><svg style="left:273px;fill:var(--gold)"><use href="#jersey"/></svg><span style="left:302px">vs.</span><i style="left:339px"></i><span style="left:352px">Top Shelf Crew</span><i style="left:487px"></i><svg style="left:502px;fill:var(--red)"><use href="#jersey"/></svg><i style="left:543px"></i><span style="left:561px">Maple Centre</span><i style="left:703px"></i></div>
      </div>
    </section>

    <section class="day" style="top:206px">
      <div class="date">Wednesday Oct 6th</div>
      <div class="table">
        <div class="thead"><span style="left:57px">TIME</span><span style="left:161px">HOME</span><span style="left:385px">AWAY</span><span style="left:580px">LOCATION</span><span style="left:732px">STICK</span></div>
        <div class="row" style="top:25px"><span style="left:12px">RS</span><span style="left:48px">8:00pm</span><i style="left:133px"></i><span style="left:164px">KODIAK</span><i style="left:246px"></i><svg style="left:273px;fill:var(--gold)"><use href="#jersey"/></svg><span style="left:302px">vs.</span><i style="left:339px"></i><span style="left:352px">Top Shelf Crew</span><i style="left:487px"></i><svg style="left:502px;fill:var(--red)"><use href="#jersey"/></svg><i style="left:543px"></i><span style="left:561px">Maple Centre</span><i style="left:703px"></i></div>
        <div class="row" style="top:64px"><span style="left:12px">RS</span><span style="left:48px">8:00pm</span><i style="left:133px"></i><span style="left:164px">KODIAK</span><i style="left:246px"></i><svg style="left:273px;fill:var(--gold)"><use href="#jersey"/></svg><span style="left:302px">vs.</span><i style="left:339px"></i><span style="left:352px">Top Shelf Crew</span><i style="left:487px"></i><svg style="left:502px;fill:var(--red)"><use href="#jersey"/></svg><i style="left:543px"></i><span style="left:561px">Maple Centre</span><i style="left:703px"></i></div>
        <div class="row last" style="top:103px"><span style="left:12px">RS</span><span style="left:48px">8:00pm</span><i style="left:133px"></i><span style="left:164px">KODIAK</span><i style="left:246px"></i><svg style="left:273px;fill:var(--gold)"><use href="#jersey"/></svg><span style="left:302px">vs.</span><i style="left:339px"></i><span style="left:352px">Top Shelf Crew</span><i style="left:487px"></i><svg style="left:502px;fill:var(--red)"><use href="#jersey"/></svg><i style="left:543px"></i><span style="left:561px">Maple Centre</span><i style="left:703px"></i></div>
      </div>
    </section>

    <section class="day" style="top:405px">
      <div class="date">Wednesday Oct 6th</div>
      <div class="table">
        <div class="thead"><span style="left:57px">TIME</span><span style="left:161px">HOME</span><span style="left:385px">AWAY</span><span style="left:580px">LOCATION</span><span style="left:732px">STICK</span></div>
        <div class="row" style="top:25px"><span style="left:12px">RS</span><span style="left:48px">8:00pm</span><i style="left:133px"></i><span style="left:164px">KODIAK</span><i style="left:246px"></i><svg style="left:273px;fill:var(--gold)"><use href="#jersey"/></svg><span style="left:302px">vs.</span><i style="left:339px"></i><span style="left:352px">Top Shelf Crew</span><i style="left:487px"></i><svg style="left:502px;fill:var(--red)"><use href="#jersey"/></svg><i style="left:543px"></i><span style="left:561px">Maple Centre</span><i style="left:703px"></i></div>
        <div class="row" style="top:64px"><span style="left:12px">RS</span><span style="left:48px">8:00pm</span><i style="left:133px"></i><span style="left:164px">KODIAK</span><i style="left:246px"></i><svg style="left:273px;fill:var(--gold)"><use href="#jersey"/></svg><span style="left:302px">vs.</span><i style="left:339px"></i><span style="left:352px">Top Shelf Crew</span><i style="left:487px"></i><svg style="left:502px;fill:var(--red)"><use href="#jersey"/></svg><i style="left:543px"></i><span style="left:561px">Maple Centre</span><i style="left:703px"></i></div>
        <div class="row last" style="top:103px"><span style="left:12px">RS</span><span style="left:48px">8:00pm</span><i style="left:133px"></i><span style="left:164px">KODIAK</span><i style="left:246px"></i><svg style="left:273px;fill:var(--gold)"><use href="#jersey"/></svg><span style="left:302px">vs.</span><i style="left:339px"></i><span style="left:352px">Top Shelf Crew</span><i style="left:487px"></i><svg style="left:502px;fill:var(--red)"><use href="#jersey"/></svg><i style="left:543px"></i><span style="left:561px">Maple Centre</span><i style="left:703px"></i></div>
      </div>
    </section>

    <section class="day" style="top:604px">
      <div class="date">Wednesday Oct 6th</div>
      <div class="table">
        <div class="thead"><span style="left:57px">TIME</span><span style="left:161px">HOME</span><span style="left:385px">AWAY</span><span style="left:580px">LOCATION</span><span style="left:732px">STICK</span></div>
        <div class="row" style="top:25px"><span style="left:12px">RS</span><span style="left:48px">8:00pm</span><i style="left:133px"></i><span style="left:164px">KODIAK</span><i style="left:246px"></i><svg style="left:273px;fill:var(--gold)"><use href="#jersey"/></svg><span style="left:302px">vs.</span><i style="left:339px"></i><span style="left:352px">Top Shelf Crew</span><i style="left:487px"></i><svg style="left:502px;fill:var(--red)"><use href="#jersey"/></svg><i style="left:543px"></i><span style="left:561px">Maple Centre</span><i style="left:703px"></i></div>
        <div class="row" style="top:64px"><span style="left:12px">RS</span><span style="left:48px">8:00pm</span><i style="left:133px"></i><span style="left:164px">KODIAK</span><i style="left:246px"></i><svg style="left:273px;fill:var(--gold)"><use href="#jersey"/></svg><span style="left:302px">vs.</span><i style="left:339px"></i><span style="left:352px">Top Shelf Crew</span><i style="left:487px"></i><svg style="left:502px;fill:var(--red)"><use href="#jersey"/></svg><i style="left:543px"></i><span style="left:561px">Maple Centre</span><i style="left:703px"></i></div>
        <div class="row last" style="top:103px"><span style="left:12px">RS</span><span style="left:48px">8:00pm</span><i style="left:133px"></i><span style="left:164px">KODIAK</span><i style="left:246px"></i><svg style="left:273px;fill:var(--gold)"><use href="#jersey"/></svg><span style="left:302px">vs.</span><i style="left:339px"></i><span style="left:352px">Top Shelf Crew</span><i style="left:487px"></i><svg style="left:502px;fill:var(--red)"><use href="#jersey"/></svg><i style="left:543px"></i><span style="left:561px">Maple Centre</span><i style="left:703px"></i></div>
      </div>
    </section>

    <aside>
      <div class="box" style="top:38px">
        <h3>SCHEDULES</h3>
        <ul><li>Division A</li><li>Division B</li><li>Division C</li><li>All Divisions</li><li>Playoffs</li></ul>
      </div>
      <div class="box" style="top:214px">
        <h3>START MENU</h3>
        <ul><li>Game Rules</li><li>Scoreboard</li><li>Standings</li><li>Leaders</li></ul>
      </div>
      <div class="box" style="top:367px">
        <h3>QUICK LINKS</h3>
        <ul><li>Rules</li><li>Teams</li><li>News</li><li>Free Agents</li><li>Champ T-Shirt Request</li></ul>
      </div>
      <div class="login abs">LOGIN &nbsp;&nbsp;&nbsp;&nbsp;&nbsp;&#9658;</div>
    </aside>
  </main>

  <footer class="abs footer">© 2011-2012, SPORTS. ALL RIGHTS RESERVED, Data Feed by leaguefeed.net</footer>
</div>
</body>
</html>
```